Business card for law firm

Need business card for new law firm. Think confident, authoritative, conservative, but not stuffy or old-fashioned.

Contact Information for Business Card

Content for card - logo (uploaded), plus the following:

Paul Wexbury (larger font)
Managing Partner (larger font, but not as large as name)
Level 9, 41 Tansy Lane
Sydney NSW 2000
Main Tel 02 7346 2190
Direct Tel 02 6273 4415
Email paul@qvlegal.com.au
www.qvlegal.com.au

Letterhead design should include logo plus:
Level 9, 41 Tansy Lane
Sydney NSW 2000
Tel 02 6273 4415
www.qvlegal.com.au

```html
<!DOCTYPE html>
<html lang="en">
<head>
<meta charset="utf-8">
<title>Quayvale Lawyers – Business Card</title>
<link rel="stylesheet" href="https://fonts.googleapis.com/css2?family=Open+Sans:wght@400;700&display=swap">
<style>
  :root {
    --backdrop: #d8d5d1;
    --card: #1d1e20;
    --card-edge: #141516;
    --white: #f4f4f4;
    --silver: #b9bbbe;
  }
  * { margin: 0; padding: 0; box-sizing: border-box; }
  html, body {
    width: 1200px;
    height: 864px;
    overflow: hidden;
    background: var(--backdrop);
  }
  .sheet {
    width: 1200px;
    height: 864px;
    display: flex;
    align-items: center;
    justify-content: center;
    gap: 40px;
  }
  .card {
    position: relative;
    width: 540px;
    height: 330px;
    background: var(--card);
    border: 1px solid var(--card-edge);
    box-shadow: 0 10px 24px rgba(0,0,0,0.25);
    color: var(--white);
    font-family: "Open Sans", sans-serif;
  }

  /* Wordmark: invented name in the card's text font, one colour, one weight */
  .wordmark {
    display: flex;
    align-items: center;
    gap: 12px;
  }
  .wordmark__square {
    width: 18px;
    height: 18px;
    flex: none;
    background: currentColor;
  }
  .wordmark__name {
    font-family: "Open Sans", sans-serif;
    font-weight: 400;
    font-size: 24px;
    line-height: 1;
    white-space: nowrap;
  }

  /* Front */
  .card--front {
    display: flex;
    flex-direction: column;
    align-items: center;
    justify-content: center;
  }
  .card--front .wordmark { color: var(--silver); }
  .card--front .wordmark__name { font-size: 28px; }
  .front__web {
    margin-top: 40px;
    font-size: 14px;
    letter-spacing: 6px;
    color: var(--silver);
  }

  /* Back */
  .card--back .wordmark {
    position: absolute;
    left: 28px;
    top: 152px;
    color: var(--white);
  }
  .card--back .wordmark__name { font-size: 21px; }
  .divider {
    position: absolute;
    left: 296px;
    top: 70px;
    width: 2px;
    height: 200px;
    background: linear-gradient(to bottom, rgba(255,255,255,0), var(--white) 30%, var(--white) 70%, rgba(255,255,255,0));
  }
  .details {
    position: absolute;
    left: 318px;
    top: 84px;
    color: var(--white);
  }
  .details__name {
    font-size: 19px;
    font-weight: 700;
    text-transform: uppercase;
    line-height: 1.1;
  }
  .details__role {
    font-size: 13px;
    font-weight: 700;
    text-transform: uppercase;
    margin-bottom: 10px;
  }
  .details__address {
    font-size: 14px;
    line-height: 1.3;
    margin-bottom: 4px;
    font-style: normal;
  }
  .contact-list { list-style: none; }
  .contact-list li {
    display: flex;
    align-items: center;
    gap: 8px;
    font-size: 14px;
    line-height: 1.35;
  }
  .contact-list svg {
    width: 12px;
    height: 12px;
    flex: none;
    fill: none;
    stroke: var(--white);
    stroke-width: 1.6;
  }
</style>
</head>
<body>
<main class="sheet">
  <section class="card card--front" aria-label="Card front">
    <div class="wordmark">
      <span class="wordmark__square"></span>
      <span class="wordmark__name">Quayvale Lawyers</span>
    </div>
    <p class="front__web">www.qvlegal.com.au</p>
  </section>

  <section class="card card--back" aria-label="Card back">
    <div class="wordmark">
      <span class="wordmark__square"></span>
      <span class="wordmark__name">Quayvale Lawyers</span>
    </div>
    <div class="divider"></div>
    <div class="details">
      <p class="details__name">Paul Wexbury</p>
      <p class="details__role">Managing Partner</p>
      <address class="details__address">Level 9, 41 Tansy Lane<br>Sydney NSW 2000</address>
      <ul class="contact-list">
        <li>
          <svg viewBox="0 0 12 12" aria-hidden="true"><path d="M2 3c0-1 1-1.5 4-1.5S10 2 10 3v1H8V3H4v1H2z M3 5h6l1 5H2z"/></svg>
          02 7346 2190
        </li>
        <li>
          <svg viewBox="0 0 12 12" aria-hidden="true"><rect x="3" y="1" width="6" height="10" rx="1"/><line x1="5" y1="9" x2="7" y2="9"/></svg>
          02 6273 4415
        </li>
        <li>
          <svg viewBox="0 0 12 12" aria-hidden="true"><rect x="1" y="2.5" width="10" height="7"/><polyline points="1,2.5 6,6.5 11,2.5"/></svg>
          paul@qvlegal.com.au
        </li>
        <li>
          <svg viewBox="0 0 12 12" aria-hidden="true"><circle cx="6" cy="6" r="5"/><ellipse cx="6" cy="6" rx="2" ry="5"/><line x1="1" y1="6" x2="11" y2="6"/></svg>
          www.qvlegal.com.au
        </li>
      </ul>
    </div>
  </section>
</main>
</body>
</html>
```